Refresh web site from year 2003

Voltaro Works has a web site (https://vowrk-site.no/) from early 2000 that needs to be refreshed.

Attached are company logo, favicon files, a licensed image to be used, an animation that illustrate the use of one of the products.

Target Market(s)

Industrial customers

Industry/Entity Type

Electrical Switch Board Builders, Automation Industry

Coding

Coded - Design and coding required

Number of Pages Required

3 page

Requirements
Must have
• WordPress site. Use attached animation in the front page (source file is in Adobe Animation format, if adjustments are needed). Product page for two products, "KTR" and "QX-7 Ver B".
Nice to have
• The site should focus on promoting two products KTR and QX-7 Ver B.

```html
<!DOCTYPE html>
<html lang="en">
<head>
<meta charset="utf-8">
<title>Voltaro Works</title>
<link rel="stylesheet" href="https://fonts.googleapis.com/css2?family=Montserrat:wght@500;600;700;800;900&family=Open+Sans:wght@400;600&display=swap">
<style>
:root{
  --brand:#0b4a86;
  --brand-deep:#083c70;
  --hero-a:#2a5f98;
  --hero-b:#14406f;
  --ink:#333a44;
  --muted:#6b6f75;
  --white:#ffffff;
  --footer:#343434;
  --card-line:#e6e8ec;
}
*{margin:0;padding:0;box-sizing:border-box}
html,body{width:1200px;height:2620px;overflow:hidden;background:var(--white)}
body{position:relative;font-family:"Open Sans",Arial,sans-serif;color:var(--ink)}
.abs{position:absolute}
.heading{font-family:"Montserrat",Arial,sans-serif}

/* hero */
.hero{left:0;top:0;width:1200px;height:577px;background:linear-gradient(100deg,var(--hero-a) 0%,#245a94 45%,var(--hero-b) 100%)}
.brand-name{font-family:"Montserrat",Arial,sans-serif;font-weight:800;color:var(--white);line-height:1.05}
.hero .brand-name{left:194px;top:22px;font-size:24px;width:170px}
.menu-toggle{left:984px;top:34px}
.social{left:32px;width:16px;height:16px;border:2px solid var(--white);border-radius:50%}
.side-label{left:41px;top:330px;transform:translate(-50%,-50%) rotate(-90deg);font-family:"Montserrat",Arial,sans-serif;font-weight:700;font-size:14px;letter-spacing:1.5px;color:var(--white);white-space:nowrap}
.hero-kicker{left:193px;top:146px;font-size:26px;font-weight:800;letter-spacing:4px;color:var(--white)}
.hero-title{left:190px;top:186px;font-size:63px;font-weight:900;line-height:60px;color:var(--white);letter-spacing:0.5px}
.hero-text{left:193px;top:320px;width:340px;font-size:14.5px;line-height:20.5px;color:var(--white)}
.btn-outline{left:195px;top:415px;width:143px;height:38px;border:2px solid var(--white);border-radius:3px;color:var(--white);font-family:"Montserrat",Arial,sans-serif;font-weight:700;font-size:11.5px;display:flex;align-items:center;justify-content:center;gap:8px}

/* products */
.section-kicker{left:0;width:1200px;text-align:center;font-family:"Montserrat",Arial,sans-serif;font-weight:600;font-size:14px;letter-spacing:3px;color:var(--ink)}
.section-title{left:0;width:1200px;text-align:center;font-family:"Montserrat",Arial,sans-serif;font-weight:800;font-size:34px;letter-spacing:1.5px;color:var(--brand)}
.product-tile{top:756px;height:303px;width:270px}
.btn-solid{left:522px;top:1091px;width:156px;height:44px;background:var(--brand);color:var(--white);font-family:"Montserrat",Arial,sans-serif;font-weight:700;font-size:11.5px;display:flex;align-items:center;justify-content:center}

/* about */
.about-band{left:0;top:1353px;width:603px;height:428px;background:var(--brand)}
.about-photo{left:603px;top:1269px;width:597px;height:593px;background:linear-gradient(135deg,#d9dde2 0%,#b9c4cf 35%,#3d66b0 60%,#4d7a4e 90%);box-shadow:0 30px 50px rgba(0,0,0,.18)}
.about-inset{left:475px;top:1627px;width:226px;height:207px;background:linear-gradient(140deg,#9fb7cf 0%,#dfe6ee 45%,#3a6eb1 80%)}
.about-rule{left:130px;top:1455px;width:82px;height:2px;background:var(--white)}
.about-title{left:227px;top:1433px;font-size:44px;font-weight:900;line-height:43px;color:var(--white);letter-spacing:1px}
.about-text{left:227px;top:1537px;width:234px;font-size:8.6px;line-height:12px;color:var(--white)}
.about-sub{left:227px;top:1635px;font-size:12.5px;font-weight:800;color:var(--white);letter-spacing:.5px}
.slide-btn{top:1673px;width:28px;height:27px;background:var(--white);display:flex;align-items:center;justify-content:center}

/* services */
.service-card{top:2055px;width:242px;height:216px;background:var(--white);border:1px solid var(--card-line);box-shadow:0 4px 14px rgba(0,0,0,.06);text-align:center}
.service-card.is-active{background:var(--brand);border-color:var(--brand)}
.service-card svg{margin-top:44px}
.service-title{margin-top:10px;font-family:"Montserrat",Arial,sans-serif;font-weight:800;font-size:17px;letter-spacing:1px;color:var(--brand)}
.service-text{margin:6px auto 0;width:200px;font-size:9.6px;line-height:14px;color:var(--muted)}
.is-active .service-title,.is-active .service-text{color:var(--white)}
.is-active .service-text{font-weight:600}

/* footer */
.footer{left:0;top:2378px;width:1200px;height:242px;background:var(--footer)}
.footer .brand-name{left:194px;top:2428px;font-size:23px;width:160px}
.footer-text{left:194px;top:2510px;width:205px;font-family:Arial,sans-serif;font-size:12.5px;line-height:16px;color:var(--white)}
.footer-head{top:2422px;font-family:"Montserrat",Arial,sans-serif;font-weight:600;font-size:20px;color:var(--white)}
.footer-links{top:2462px;list-style:none;font-family:"Montserrat",Arial,sans-serif;font-weight:500;font-size:12px;color:var(--white)}
.footer-links li{height:23.6px}
.contact-line{font-family:"Montserrat",Arial,sans-serif;font-weight:500;font-size:12px;color:var(--white);display:flex;align-items:center;gap:6px}
</style>
</head>
<body>

<!-- hero -->
<section class="abs hero" role="img" aria-label="Electrical switchboard panels with buttons and dials, tinted blue"></section>
<div class="abs brand-name">Voltaro<br>Works</div>
<svg class="abs menu-toggle" width="22" height="20" viewBox="0 0 22 20" aria-label="Menu">
  <rect x="0" y="1" width="22" height="3.5" rx="1.5" fill="#fff"/>
  <rect x="0" y="8.5" width="22" height="3.5" rx="1.5" fill="#fff"/>
  <rect x="0" y="16" width="22" height="3.5" rx="1.5" fill="#fff"/>
</svg>
<span class="abs social" style="top:96px"></span>
<span class="abs social" style="top:128px"></span>
<div class="abs side-label">LED PODUCTS</div>
<div class="abs heading hero-kicker">WELCOME TO</div>
<h1 class="abs heading hero-title">VOLTARO<br>WORKS</h1>
<p class="abs hero-text">Voltaro Works is a production and development company for electronics with emphasis on small series production.</p>
<a class="abs btn-outline">DISCOVER MORE
  <svg width="7" height="11" viewBox="0 0 7 11"><path d="M1 1l4.5 4.5L1 10" stroke="#fff" stroke-width="1.8" fill="none"/></svg>
</a>

<!-- products -->
<div class="abs section-kicker" style="top:668px">VOLTARO WORKS</div>
<h2 class="abs section-title" style="top:684px">LED PODUCTS</h2>
<div class="abs product-tile" style="left:192px;background:linear-gradient(135deg,#f2f2f2 0%,#2c3a66 45%,#c6c6c6 75%,#e9a23a 100%)" role="img" aria-label="Boxed automotive LED bulb pair"></div>
<div class="abs product-tile" style="left:463px;width:271px;background:linear-gradient(160deg,#dcdcdc 0%,#c44a3c 30%,#3b8f4a 55%,#e7b02a 85%)" role="img" aria-label="Hand pressing coloured buttons on a control panel"></div>
<div class="abs product-tile" style="left:735px;background:linear-gradient(180deg,#5a2bd8 0%,#b24ee6 30%,#f0508a 55%,#f4e27a 80%,#d8f4f8 100%)" role="img" aria-label="Row of glowing LED lights in purple and warm tones"></div>
<a class="abs btn-solid">VIEW MORE PRODUCTS</a>

<!-- about -->
<div class="abs about-band"></div>
<div class="abs about-photo" role="img" aria-label="Technician soldering a circuit board in an electronics workshop"></div>
<div class="abs about-inset" role="img" aria-label="Engineer assembling electronics in a clean production hall"></div>
<div class="abs about-rule"></div>
<h2 class="abs heading about-title">VOLTARO<br>WORKS</h2>
<p class="abs about-text">Voltaro Works is a production and development company for electronics with emphasis on small series production. We are today two employees with good and relevant access to additional expertise in the established network. The company was established in 1985 and has since 2001 taken over production equipment and production basis from another company in the same industry.</p>
<div class="abs heading about-sub">FERRAND CIRCUITS</div>
<span class="abs slide-btn" style="left:227px"><svg width="6" height="9" viewBox="0 0 6 9"><path d="M5 1L1.5 4.5 5 8" stroke="#222" stroke-width="1.5" fill="none"/></svg></span>
<span class="abs slide-btn" style="left:261px"><svg width="6" height="9" viewBox="0 0 6 9"><path d="M1 1l3.5 3.5L1 8" stroke="#222" stroke-width="1.5" fill="none"/></svg></span>

<!-- services -->
<h2 class="abs section-title" style="top:1980px">OUR SERVICES</h2>

<div class="abs service-card" style="left:193px">
  <svg width="46" height="44" viewBox="0 0 46 44" fill="none" stroke="#0b4a86" stroke-width="1.6">
    <rect x="4" y="2" width="38" height="6"/><path d="M17 8v8h12V8M14 16h18l-4 10H18z"/><path d="M23 26v6"/><path d="M2 40h42"/><path d="M10 34l-3 4M36 34l3 4M16 32l-1 4M30 32l1 4"/>
  </svg>
  <div class="service-title">PRODUCTION</div>
  <p class="service-text">Small series production of electronic units in the number of 10 to 200 units.</p>
</div>

<div class="abs service-card is-active" style="left:479px">
  <svg width="46" height="44" viewBox="0 0 46 44" fill="none" stroke="#fff" stroke-width="1.6">
    <path d="M23 4l4 1 2 4 4-1 3 3-1 4 4 2 1 4-1 4-4 2 1 4-3 3-4-1-2 4-4 1-4-1-2-4-4 1-3-3 1-4-4-2-1-4 1-4 4-2-1-4 3-3 4 1 2-4z"/><circle cx="23" cy="22" r="7"/><path d="M23 22h16M23 16h12M23 28h12"/>
  </svg>
  <div class="service-title">DEVOLEPMENT</div>
  <p class="service-text">Development of product concept to finished product in collaboration with a customer.</p>
</div>

<div class="abs service-card" style="left:763px">
  <svg width="46" height="44" viewBox="0 0 46 44" fill="none" stroke="#0b4a86" stroke-width="1.6">
    <path d="M23 2a13 13 0 0 0-8 23c2 2 3 4 3 7h10c0-3 1-5 3-7A13 13 0 0 0 23 2z"/><circle cx="23" cy="15" r="5"/><circle cx="23" cy="15" r="1.5"/><path d="M18 36h10M19 40h8"/>
  </svg>
  <div class="service-title">DESIGN</div>
  <p class="service-text">Designing of electronics and print cards for pre-assembled and tested unit.</p>
</div>

<!-- footer -->
<footer class="abs footer"></footer>
<div class="abs brand-name">Voltaro<br>Works</div>
<p class="abs footer-text">Lorem ipsum dolor sit amet, consec tetur adipiscing elit, sed do eiusmod tempor incididunt ut labore et dolore magna aliqua.</p>

<div class="abs footer-head" style="left:440px">QUICK LINKS</div>
<ul class="abs footer-links" style="left:441px">
  <li>Home</li><li>Licenses</li><li>Privacy Policy</li><li>Join Our Team</li>
</ul>

<div class="abs footer-head" style="left:643px">RESOURCES</div>
<ul class="abs footer-links" style="left:644px">
  <li>Get a Quote</li><li>Apply Now</li><li>Login</li><li>Calculators</li><li>Blog</li>
</ul>

<div class="abs footer-head" style="left:818px">CONTACT US</div>
<div class="abs contact-line" style="left:818px;top:2463px">
  <svg width="12" height="9" viewBox="0 0 12 9"><rect x="0" y="0" width="12" height="9" rx="1" fill="#fff"/><path d="M0.5 0.8L6 5l5.5-4.2" stroke="#343434" stroke-width="1.2" fill="none"/></svg>
  Email: post@voltaro-mail.no
</div>
<div class="abs contact-line" style="left:818px;top:2485px">
  <svg width="11" height="11" viewBox="0 0 11 11"><path d="M2 0.5l2 2.5-1.2 1.4a7 7 0 0 0 3.8 3.8L8 7l2.5 2-1 1.5C5 10.5 0.5 6 0.5 1.5z" fill="#fff"/></svg>
  Phone: +47 612 48 370
</div>
<div class="abs contact-line" style="left:818px;top:2526px">
  <svg width="9" height="12" viewBox="0 0 9 12"><path d="M4.5 0A4.5 4.5 0 0 0 0 4.5C0 8 4.5 12 4.5 12S9 8 9 4.5A4.5 4.5 0 0 0 4.5 0z" fill="#fff"/><circle cx="4.5" cy="4.5" r="1.6" fill="#343434"/></svg>
  Address: Voltaro Works
</div>
<div class="abs contact-line" style="left:818px;top:2547px">N-5120 Dalvik</div>
<div class="abs contact-line" style="left:818px;top:2568px">Norway</div>

</body>
</html>
```